Letterhead Design Project

We have recently updated our corporate logo and are seeking a new letterhead template.

Attached is the new logo and the old letterhead.

PLEASE DO NOT USE OUR EXISTING WEB SITE FOR INSPIRATION as we are redesigning it.

Target Market(s)

Executives, search professionals, technical and scientific professionals

Industry/Entity Type

Seeking

```html
<!DOCTYPE html>
<html lang="en">
<head>
<meta charset="utf-8">
<title>HelixSeek Stationery</title>
<link href="https://fonts.googleapis.com/css2?family=Nunito:wght@700&family=Open+Sans:wght@400;600&family=Tinos&display=swap" rel="stylesheet">
<style>
:root{
  --backdrop:#8a8a8a;
  --paper:#ffffff;
  --brand-blue:#0a8fcf;
  --deep-blue:#0a7dbf;
  --sky:#66d3ff;
  --ink:#1f1f1f;
  --muted:#8c8c8c;
}
*{margin:0;padding:0;box-sizing:border-box}
html,body{width:1200px;height:900px;overflow:hidden;background:var(--backdrop)}
.canvas{position:relative;width:1200px;height:900px}
.sheet{position:absolute;background:var(--paper);overflow:hidden}
.sheet svg.wave{position:absolute;left:0;top:0}
.brand{position:absolute;display:flex;align-items:center;gap:5px;font-family:"Nunito",sans-serif;font-weight:700;color:var(--brand-blue);white-space:nowrap}
.brand .dot{border-radius:50%;background:var(--brand-blue)}

/* letterhead */
.letterhead{left:382px;top:64px;width:442px;height:587px}
.letterhead .brand{left:15px;top:26px;font-size:17px}
.letterhead .brand .dot{width:17px;height:17px}
.lh-contact{position:absolute;left:287px;top:22px;font-family:"Open Sans",sans-serif;font-size:6.6px;line-height:7.3px;color:var(--ink)}
.lh-aside{position:absolute;left:300px;top:116px;width:100px;font-family:"Tinos",serif;font-size:6px;line-height:9.6px;color:var(--ink)}
.lh-aside p{text-indent:11px}
.lh-salutation{position:absolute;left:51px;top:161px;font-family:"Open Sans",sans-serif;font-size:8.5px;color:var(--ink)}
.lh-body{position:absolute;left:50px;top:193px;width:348px;font-family:"Tinos",serif;font-size:7.4px;line-height:11.45px;color:var(--ink);text-align:justify}
.lh-body p{text-indent:18px}
.lh-body p.gap{margin-top:23px}
.lh-body p.gap-sm{margin-top:11px}
.lh-closing{position:absolute;left:54px;top:503px;font-family:"Open Sans",sans-serif;font-size:8.5px;color:var(--ink)}
.lh-date{position:absolute;left:54px;top:551px;font-family:"Open Sans",sans-serif;font-size:7px;color:#6c8ea0}
.lh-signer{position:absolute;left:341px;top:493px;font-family:"Open Sans",sans-serif;font-size:7px;line-height:7.4px;color:var(--muted)}
.lh-signature{position:absolute;left:320px;top:524px;width:96px;height:36px;background:linear-gradient(90deg,#f1f1f1,#e6e6e6);border-radius:3px}
.lh-address{position:absolute;right:13px;top:563px;text-align:right;font-family:"Open Sans",sans-serif;font-size:6px;line-height:8.8px;color:var(--muted)}

/* business card */
.card-front{left:382px;top:726px;width:180px;height:119px}
.card-front .brand{left:6px;top:13px;font-size:10.5px;gap:3px}
.card-front .brand .dot{width:10px;height:10px}
.cf-name{position:absolute;left:6px;top:43px;font-family:"Open Sans",sans-serif;font-weight:600;font-size:10px;color:var(--brand-blue)}
.cf-title{position:absolute;left:6px;top:56px;font-family:"Open Sans",sans-serif;font-size:7.5px;color:var(--brand-blue)}
.cf-contact{position:absolute;left:6px;top:79px;font-family:"Open Sans",sans-serif;font-size:4px;line-height:4.6px;color:var(--ink)}
.cf-address{position:absolute;left:6px;top:94px;font-family:"Open Sans",sans-serif;font-size:4px;line-height:4.8px;color:var(--ink)}
.cf-web{position:absolute;left:8px;top:107px;font-family:"Open Sans",sans-serif;font-size:5.5px;color:var(--ink)}
.cf-disc{position:absolute;left:92px;top:22px;width:80px;height:80px;border-radius:50%;background:var(--brand-blue)}

.card-back{left:643px;top:726px;width:180px;height:120px}
.card-back .brand{left:18px;top:50px;font-size:17px}
.card-back .brand .dot{width:17px;height:17px}
</style>
</head>
<body>
<div class="canvas">

  <section class="sheet letterhead">
    <svg class="wave" width="442" height="587" viewBox="0 0 442 587" aria-hidden="true">
      <path d="M0 0 H442 V8 H0 Z" fill="var(--deep-blue)"/>
      <path d="M0 8 H150 C170 8 190 10 210 14 H0 Z" fill="var(--sky)"/>
      <path d="M185 8 H442 V72 C380 66 300 58 270 38 C250 24 225 14 185 8 Z" fill="var(--sky)"/>
      <path d="M380 0 H442 V34 C425 26 405 14 380 0 Z" fill="var(--deep-blue)"/>
      <path d="M0 515 C90 505 190 530 262 587 H0 Z" fill="var(--sky)"/>
    </svg>

    <div class="brand"><span class="dot"></span>HelixSeek</div>
    <div class="lh-contact">
      phone: 555.210.0100<br>
      fax: &nbsp;&nbsp;&nbsp;&nbsp;555.210.0110<br>
      email: office@helixseek.com
    </div>

    <div class="lh-aside">
      <p>Lorem ipsum dolor sit amet, consectetur adipiscing elit. Vivamus non diam sollicitudin est posuere congue non nec lacus. Nulla sit amet odio a est fringilla dictum vel ut nulla. Sed a mauris</p>
    </div>

    <div class="lh-salutation">Dear ipsum</div>

    <div class="lh-body">
      <p>Lorem ipsum dolor sit amet, consectetur adipiscing elit. Vivamus non diam sollicitudin est posuere congue non nec lacus. Nulla sit amet odio a est fringilla dictum vel ut nulla. Sed a mauris elit. Proin convallis mi rhoncus nisl commodo tempus. Pellentesque sollicitudin feugiat nibh, ut sagittis arcu elementum sed. Suspendisse pulvinar vehicula vestibulum. Nam ultricies erat et eros aliquet dictum. Cras tempus nunc a justo interdum vitae porta arcu scelerisque. Sed volutpat nunc et diam volutpat fringilla. Ut sit amet risus erat.</p>
      <p>Pellentesque vel neque in sapien imperdiet condimentum eu in erat. Aenean pulvinar mauris ac turpis pretium a tristique metus placerat. Nunc at nulla id sem mollis tristique nec ut ligula. In hac habitasse platea dictumst. Cras commodo lobortis luctus.</p>
      <p class="gap">Sed auctor elit ac mauris consequat molestie. Donec at velit a libero convallis venenatis. Curabitur commodo rutrum congue. Vestibulum et odio diam, ac adipiscing quam. Aenean at iaculis nisi. Aliquam a dolor nec justo rutrum vestibulum. Vivamus posuere augue eu odio vehicula ut ornare purus laoreet. Aenean at vestibulum turpis. Fusce fringilla, elit nec sagittis pellentesque, nisi diam sagittis dui, ac eleifend leo turpis non nunc. Nunc ut mauris neque. Sed blandit egestas nunc, hendrerit commodo tellus hendrerit ut.</p>
      <p class="gap-sm">Etiam at diam sit amet dui ultrices mattis in ac dolor. Vestibulum id arcu ut nulla venenatis vestibulum. Etiam in lectus ante, in laoreet arcu. Etiam fringilla eros eu neque rutrum feugiat. Suspendisse dictum, tellus sit amet suscipit cursus, est elit auctor justo, ut tincidunt leo elit ac dui. Morbi iaculis, nunc quis facilisis mattis, nunc nisl porttitor tellus, vel dictum ante nunc nec tortor. Suspendisse rhoncus libero eget tortor molestie semper. Aenean erat dui, cursus sit amet imperdiet quis, mollis non nisi. Praesent ornare laoreet mi, ut pellentesque mi vulputate at.</p>
    </div>

    <div class="lh-closing">Ipsum</div>
    <div class="lh-date">Date</div>
    <div class="lh-signer">Maren T. Ellison<br>President</div>
    <div class="lh-signature" role="img" aria-label="Handwritten signature of the president"></div>
    <div class="lh-address">48 Harbor Lane, Suite 120<br>Northvale, MA 01999</div>
  </section>

  <section class="sheet card-front">
    <div class="brand"><span class="dot"></span>HelixSeek</div>
    <div class="cf-name">Maren T. Ellison</div>
    <div class="cf-title">President</div>
    <div class="cf-contact">phone: 555.210.0100<br>fax: &nbsp;&nbsp;&nbsp;555.210.0110<br>email: office@helixseek.com</div>
    <div class="cf-address">48 Harbor Lane, Suite 120<br>Northvale, MA 01999</div>
    <div class="cf-web">www.helixseek.com</div>
    <div class="cf-disc" aria-hidden="true"></div>
  </section>

  <section class="sheet card-back">
    <svg class="wave" width="180" height="120" viewBox="0 0 180 120" aria-hidden="true">
      <path d="M0 0 H180 V22 C140 32 90 20 50 24 C30 26 12 28 0 30 Z" fill="var(--brand-blue)"/>
      <path d="M0 120 V102 C40 92 90 104 130 98 C150 95 166 92 180 90 V120 Z" fill="var(--brand-blue)"/>
    </svg>
    <div class="brand"><span class="dot"></span>HelixSeek</div>
  </section>

</div>
</body>
</html>
```